Harlow Finch Ltd. Recruitment Brochure

A 12pp A4 portrait brochure is required. It should have a contemporary and modern feel to it.

Please feel free to bring the flow chart to life with symbols that reflect the title of the stage in the flow chart.

Similarly the services that are offered should be brought to life.

See the attached brief for the detailed copy and brand colour details. I have also attached the logo and imagery to be used although we are open to additional / alternative imagery as long as it is royalty free and won't cost any additional money.

Target Market(s)

Small and medium sized businesses

Industry/Entity Type

Recruitment

Font styles to use
Serif
Sans Serif

Requirements
Must have
• See project brief.
Nice to have
• See project brief - bringing the flow chart and services aspects to life would be good.
Should not have
• See project brief.

```html
<!DOCTYPE html>
<html lang="en">
<head>
<meta charset="utf-8">
<title>Harlow Finch Ltd. – Recruitment Brochure</title>
<link href="https://fonts.googleapis.com/css2?family=Raleway:wght@300;400;600;700&family=Roboto+Condensed:wght@400;700&display=swap" rel="stylesheet">
<style>
  :root{
    --maroon:#7c1a45;
    --maroon-dark:#6a1439;
    --ink:#2b2b2b;
    --muted:#555;
    --paper:#ffffff;
    --paper-shade:#f1f1f1;
    --backdrop:#e8e5e1;
    --head:"Raleway", sans-serif;
    --body:"Roboto Condensed", sans-serif;
  }
  *{box-sizing:border-box;margin:0;padding:0}
  html,body{width:1200px;height:1200px;overflow:hidden;background:var(--backdrop)}
  .canvas{position:relative;width:1200px;height:1200px;overflow:hidden;font-family:var(--body);color:var(--ink)}
  .spread{position:absolute;width:504px;height:356px;display:flex;box-shadow:0 2px 6px rgba(0,0,0,.18)}
  .spread--cover{left:58px;top:186px}
  .spread--intro{left:638px;top:186px}
  .spread--why{left:58px;top:658px}
  .spread--approach{left:638px;top:658px}
  .page{position:relative;width:252px;height:356px;background:var(--paper);overflow:hidden}
  .page--left{background:linear-gradient(90deg,#fff 0%,#fff 80%,var(--paper-shade) 100%)}
  .page--right{background:linear-gradient(90deg,var(--paper-shade) 0%,#fff 12%,#fff 100%)}
  .page--maroon{background:var(--maroon)}
  .abs{position:absolute}
  .photo{position:absolute}
  .brand{font-family:var(--head);font-weight:700;color:var(--maroon);font-size:8px;letter-spacing:.3px;display:flex;align-items:center;gap:3px;white-space:nowrap}
  .brand__dot{width:6px;height:6px;border-radius:50%;background:var(--maroon)}
  .brand--faint{color:rgba(255,255,255,.28)}
  .brand--faint .brand__dot{background:rgba(255,255,255,.28)}
  .contact{font-size:5.4px;text-align:center;line-height:1.55;color:var(--ink)}
  .contact-icon{width:9px;height:9px;display:block;margin:0 auto 2px}
  .tagline{position:absolute;background:var(--maroon);color:#fff;font-family:var(--head);text-align:center;font-size:8.6px;line-height:1.45;display:flex;flex-direction:column;justify-content:center;letter-spacing:.2px}
  .tagline b{font-weight:700}
  .tagline span{font-weight:300}
  .url{position:absolute;left:0;right:0;text-align:center;font-size:5px}
  .para{font-size:4.3px;line-height:1.55;text-align:justify;margin-bottom:5px}
  .para--light{color:#f3e3ea}
  .inline-contact{font-size:4.6px;line-height:1.4;display:flex;align-items:center;gap:3px}
  .inline-contact svg{width:8px;height:8px;flex:none}
  .why-box{position:absolute;background:var(--maroon);color:#fff;font-family:var(--head);font-weight:600;font-size:10px;line-height:1.1;padding:7px 0 0 16px}
  .section-title{position:absolute;font-family:var(--head);font-weight:700;color:var(--maroon);font-size:6px}
  .feature{position:absolute;border-left:1.3px solid var(--maroon);padding-left:3px;width:96px}
  .feature h4{font-size:4.6px;font-weight:700;margin-bottom:1px}
  .feature p{font-size:4.1px;line-height:1.45}
  .approach-head{position:absolute;background:var(--maroon);color:#fff;padding:13px 13px 6px}
  .approach-head h2{font-family:var(--head);font-weight:600;font-size:10.5px;line-height:1.25;margin-bottom:4px}
  .approach-head p{font-size:4.1px;line-height:1.45;text-align:justify}
  .step{position:absolute;display:flex;gap:6px}
  .step__icon{width:18px;flex:none;padding-top:6px}
  .step__icon svg{width:16px;height:16px;display:block}
  .step__body h3{font-size:4.9px;font-weight:700;color:var(--maroon);margin-bottom:1px;text-transform:uppercase}
  .step__body p{font-size:4px;line-height:1.45;margin-bottom:3px;text-align:justify}
</style>
</head>
<body>
<div class="canvas">

  <!-- Spread 1: back cover + front cover -->
  <section class="spread spread--cover">
    <div class="page page--left">
      <div class="brand abs" style="left:0;right:0;top:208px;justify-content:center"><span class="brand__dot"></span>HARLOW FINCH LTD.</div>
      <div class="contact abs" style="left:0;right:0;top:250px">
        <svg class="contact-icon" viewBox="0 0 10 10"><circle cx="5" cy="5" r="4.3" fill="none" stroke="#7c1a45" stroke-width=".9"/><path d="M3.6 2.8c.3-.3.7-.2.8.1l.4.8c.1.3 0 .5-.2.6l-.3.2c.2.6.6 1 1.1 1.2l.2-.3c.2-.2.4-.2.6-.1l.8.4c.3.2.3.5.1.8-.4.5-1 .6-1.6.3C4.4 6.3 3.7 5.6 3.3 4.6c-.2-.6-.1-1.3.3-1.8z" fill="#7c1a45"/></svg>
        London: 020 4000 1234<br>Manchester: 0161 555 0198
      </div>
      <div class="contact abs" style="left:0;right:0;top:290px">
        <svg class="contact-icon" viewBox="0 0 10 10"><circle cx="5" cy="5" r="4.3" fill="none" stroke="#7c1a45" stroke-width=".9"/><rect x="2.7" y="3.2" width="4.6" height="3.4" fill="none" stroke="#7c1a45" stroke-width=".7"/><path d="M2.7 3.2 5 5l2.3-1.8" fill="none" stroke="#7c1a45" stroke-width=".7"/></svg>
        www.harlowfinch.co.uk<br>info@harlowfinch.co.uk
      </div>
    </div>
    <div class="page page--right">
      <div class="brand abs" style="right:21px;top:34px"><span class="brand__dot"></span>HARLOW FINCH LTD.</div>
      <div class="photo" role="img" aria-label="Photo of a smiling businesswoman shaking hands with a candidate across a desk in a bright office" style="left:21px;top:62px;width:209px;height:210px;background:linear-gradient(135deg,#c9c1b4 0%,#e9e6dd 45%,#8e9a7a 70%,#3a3a40 100%)"></div>
      <div class="tagline" style="left:21px;top:279px;width:209px;height:46px">
        <div><span>EXPERTS IN </span><b>DELIVERING</b></div>
        <div><b>WORLD CLASS PEOPLE </b><span>SOLUTIONS</span></div>
      </div>
      <div class="url" style="top:339px">www.harlowfinch.co.uk</div>
    </div>
  </section>

  <!-- Spread 2: intro -->
  <section class="spread spread--intro">
    <div class="page page--left">
      <div class="photo" role="img" aria-label="Photo of two businessmen in conversation seated in armchairs by tall office windows" style="left:42px;top:53px;width:210px;height:210px;background:linear-gradient(160deg,#e6e8ea 0%,#b7bcc2 40%,#5a4c44 75%,#2e2b2c 100%)"></div>
      <svg class="abs" style="left:18px;top:262px" width="234" height="40" viewBox="0 0 234 40"><polygon points="10,0 234,0 234,40 0,40" fill="#7c1a45"/></svg>
      <div class="tagline" style="left:28px;top:262px;width:224px;height:40px;background:transparent">
        <div><span>EXPERTS IN </span><b>DELIVERING SENIOR</b></div>
        <div><b>SALES RECRUITMENT </b><span>SOLUTIONS</span></div>
      </div>
      <div class="inline-contact abs" style="left:60px;top:308px">
        <svg viewBox="0 0 10 10"><circle cx="5" cy="5" r="4.3" fill="none" stroke="#7c1a45" stroke-width=".9"/><path d="M3.6 2.8c.3-.3.7-.2.8.1l.4.8c.1.3 0 .5-.2.6l-.3.2c.2.6.6 1 1.1 1.2l.2-.3c.2-.2.4-.2.6-.1l.8.4c.3.2.3.5.1.8-.4.5-1 .6-1.6.3C4.4 6.3 3.7 5.6 3.3 4.6c-.2-.6-.1-1.3.3-1.8z" fill="#7c1a45"/></svg>
        <div>London: 020 4000 1234<br>Manchester: 0161 555 0198</div>
      </div>
      <div class="inline-contact abs" style="left:168px;top:308px">
        <svg viewBox="0 0 10 10"><circle cx="5" cy="5" r="4.3" fill="none" stroke="#7c1a45" stroke-width=".9"/><rect x="2.7" y="3.2" width="4.6" height="3.4" fill="none" stroke="#7c1a45" stroke-width=".7"/><path d="M2.7 3.2 5 5l2.3-1.8" fill="none" stroke="#7c1a45" stroke-width=".7"/></svg>
        <div>www.harlowfinch.co.uk<br>info@harlowfinch.co.uk</div>
      </div>
    </div>
    <div class="page page--maroon">
      <div class="abs" style="left:62px;top:98px;width:127px">
        <p class="para para--light">At Harlow Finch, we believe in putting our clients and candidates at the heart of everything we do. That is why our ethos is firmly focused on delivering quality service to ensure the needs and expectations of our clients are not only met, but exceeded.</p>
        <p class="para para--light">We fully understand how important it is to match a client's need with a candidate's ambition and the critical impact this can have on your bottom line. We know the difference recruiting the best sales person can make in terms of your profit and growth potential.</p>
        <p class="para para--light">Finding the right person in a tough employment market can be stressful, costly, time-consuming and really difficult. Undertaking a headhunting assignment will help ensure you get the best available person who will align to your company culture and values and deliver long term growth for your business.</p>
      </div>
      <div class="brand brand--faint abs" style="left:0;right:0;top:288px;justify-content:center;font-size:9px"><span class="brand__dot"></span>HARLOW FINCH LTD.</div>
    </div>
  </section>

  <!-- Spread 3: why use us -->
  <section class="spread spread--why">
    <div class="page page--left">
      <div class="photo" role="img" aria-label="Photo of two smiling businessmen in suits reviewing documents on a tablet" style="left:21px;top:23px;width:209px;height:308px;background:linear-gradient(150deg,#4b4a52 0%,#8a7a72 35%,#d8d4d6 65%,#f2f0f2 100%)"></div>
      <div class="why-box" style="left:154px;top:290px;width:76px;height:41px">WHY<br>USE US?</div>
    </div>
    <div class="page page--right">
      <div class="abs" style="left:26px;top:71px;width:92px">
        <p class="para">We pride ourselves on our ability to deliver on every assignment and are specialists in senior sales recruitment and headhunting across a wide spectrum of roles. And we know that no two roles are the same which is why we offer a range of services to deliver to your needs.</p>
        <p class="para">But we also know the challenges of the recruitment process. Our Managing Director, Daniel Reeve, has been on the client side of this process and set up Harlow Finch after identifying a real need for a truly professional service.</p>
        <p class="para">Daniel felt huge frustration at the approach taken by many sales recruitment agencies when he was on the client side. This has ensured a commitment to embedding a quality service ethos from the top down.</p>
      </div>
      <div class="abs" style="left:134px;top:71px;width:91px">
        <p class="para">we undertake a detailed proven approach on every assignment we take on.</p>
        <p class="para">We take an empathetic approach and work in partnership with organisations to headhunt the best performing senior sales talent who will help to build profitable growth. Having considerable experience of sourcing and building effective sales teams, we recognise the importance of recruiting the correct calibre of people.</p>
        <p class="para">We know the top performing senior people are not usually looking for a role because their existing employer makes sure they are kept happy. But we are specialists in identifying, approaching and delivering that talent for our clients.</p>
      </div>
      <div class="section-title" style="left:26px;top:226px">WHAT'S MORE, WE ALSO PROVIDE:</div>
      <div class="feature" style="left:30px;top:236px"><h4>Total confidentiality</h4><p>you can be sure we will operate in a strictly confidential manner in relation to both the candidates we contact as well as your organisation.</p></div>
      <div class="feature" style="left:130px;top:236px"><h4>Full transparency</h4><p>through the head hunting process, you get complete visibility at every stage so you will know the lengths we have gone to in order to exceed your expectations</p></div>
      <div class="feature" style="left:30px;top:280px"><h4>Dedicated contact</h4><p>you will be provided with a dedicated contact who will provide you with regular updates as often as you would like.</p></div>
      <div class="feature" style="left:130px;top:280px"><h4>Complete accountability</h4><p>we will not rest until we have found you the best available person for your role.</p></div>
      <div class="feature" style="left:30px;top:319px;width:200px"><h4 style="display:inline">Extended 12 month free of charge replacement guarantee</h4><p style="display:inline"> on headhunting assignments where we undertake competency interviews alongside you.</p></div>
    </div>
  </section>

  <!-- Spread 4: proven approach -->
  <section class="spread spread--approach">
    <div class="page page--left">
      <div class="approach-head" style="left:21px;top:23px;width:209px;height:77px">
        <h2>OUR PROVEN<br>APPROACH</h2>
        <p>We know the cost and stress of hiring the wrong person is significant and has a detrimental impact on the business bottom line. That is why our commitment is to ensure you get the best person, first time, by taking the robust and proven approach below.</p>
      </div>
      <div class="step" style="left:6px;top:112px;width:228px">
        <div class="step__icon"><svg viewBox="0 0 16 16"><circle cx="5" cy="8" r="3.2" fill="#7c1a45"/><circle cx="11" cy="8" r="3.2" fill="#7c1a45"/><rect x="3" y="10" width="10" height="3" rx="1" fill="#7c1a45"/><circle cx="8" cy="3" r="1.5" fill="#7c1a45"/></svg></div>
        <div class="step__body"><h3>Understanding the brief</h3><p>we will meet with you to get a detailed understanding of both your organisation and the role. We will get under the skin of what your ambition and strategy is as this will be a key part of selling the role to a candidate. We will also complete a job profile exercise and a project brief outlining all of the details discussed.</p></div>
      </div>
      <div class="step" style="left:6px;top:160px;width:228px">
        <div class="step__icon"><svg viewBox="0 0 16 16"><rect x="2" y="1.5" width="9" height="12" fill="none" stroke="#7c1a45" stroke-width="1.2"/><circle cx="10" cy="10" r="2.8" fill="#fff" stroke="#7c1a45" stroke-width="1.2"/><line x1="12" y1="12" x2="14.5" y2="14.5" stroke="#7c1a45" stroke-width="1.4"/></svg></div>
        <div class="step__body"><h3>Research</h3><p>once you have approved the project brief, we will undertake a detailed mapping exercise which will identify all of the possible companies that might employ your perfect candidate.</p><p>We will then investigate each company to establish all of the potential candidates that exist within them, producing organograms where relevant to give you confidence a thorough search was made.</p></div>
      </div>
      <div class="step" style="left:6px;top:208px;width:228px">
        <div class="step__icon"><svg viewBox="0 0 16 16"><circle cx="3.5" cy="5" r="1.8" fill="#7c1a45"/><circle cx="12.5" cy="5" r="1.8" fill="#7c1a45"/><path d="M1.5 13V8.5h4L8 10.5l2.5-2h4V13" fill="#7c1a45"/></svg></div>
        <div class="step__body"><h3>Approaches</h3><p>once you are happy with the list of prospective candidates, we will start making approaches and presenting them with the benefits of working for your organisation.</p><p>We will also undertake any initial screening of the candidate if they have expressed an interest in progressing. This establishes location, package and suitability.</p></div>
      </div>
      <div class="step" style="left:6px;top:256px;width:228px">
        <div class="step__icon"><svg viewBox="0 0 16 16"><rect x="3" y="2.5" width="10" height="12" fill="none" stroke="#7c1a45" stroke-width="1.2"/><rect x="6" y="1.3" width="4" height="2.4" fill="#7c1a45"/><path d="M5 7l1 1 1.6-1.8M5 11l1 1 1.6-1.8" fill="none" stroke="#7c1a45" stroke-width=".9"/><line x1="9" y1="7.3" x2="11.5" y2="7.3" stroke="#7c1a45"/><line x1="9" y1="11.3" x2="11.5" y2="11.3" stroke="#7c1a45"/></svg></div>
        <div class="step__body"><h3>Assessment</h3><p>any candidates that progress through to this stage will now undergo a detailed assessment process. We will narrow down all of the candidates to a longlist of suitable candidates to progress to interview.</p><p>We will then pick the best candidates for 1st interviews which will either be in person or via video call.</p><p>Finally, those candidates who are successful at 1st interview will complete a psychometric profile to establish their characteristics and personality.</p></div>
      </div>
    </div>
    <div class="page page--right">
      <div class="step" style="left:16px;top:23px;width:218px">
        <div class="step__icon"><svg viewBox="0 0 16 16"><circle cx="8" cy="4" r="1.8" fill="#7c1a45"/><circle cx="3" cy="7" r="1.6" fill="#7c1a45"/><circle cx="13" cy="7" r="1.6" fill="#7c1a45"/><path d="M6 14V8h4v6zM1.5 14v-4.5h3V14zM11.5 14v-4.5h3V14z" fill="#7c1a45"/></svg></div>
        <div class="step__body"><h3>Shortlist meeting</h3><p>we will meet with you to present a detailed view of all shortlisted candidates. This will include the output from the 1st interview highlighting key strengths and development areas, as well as the results of the psychometric profile. We will then recommend the best candidates to meet with you.</p></div>
      </div>
      <div class="step" style="left:16px;top:66px;width:218px">
        <div class="step__icon"><svg viewBox="0 0 16 16"><circle cx="5" cy="4" r="1.8" fill="#7c1a45"/><circle cx="11" cy="4" r="1.8" fill="#7c1a45"/><path d="M3 14V7h4v7zM9 14V7h4v7z" fill="#7c1a45"/><rect x="1" y="10" width="14" height="1.2" fill="#7c1a45"/></svg></div>
        <div class="step__body"><h3>Client interviews</h3><p>once you have approved the list of candidates, we will arrange the interviews and can attend these with you if you wish. We offer an extended 12 month guarantee from our usual 6 month guarantee if we participate at this stage.</p><p>Our attendance can provide valuable competency interviewing experience as well as helping to provide an objective view of the interview performance.</p></div>
      </div>
      <div class="step" style="left:16px;top:131px;width:218px">
        <div class="step__icon"><svg viewBox="0 0 16 16"><rect x="2" y="3" width="10.5" height="10.5" fill="none" stroke="#7c1a45" stroke-width="1.4"/><path d="M4.5 8l2.5 2.5L14.5 2.5" fill="none" stroke="#7c1a45" stroke-width="1.8"/></svg></div>
        <div class="step__body"><h3>Offer and acceptance</h3><p>as soon as all interviews are completed, we will act as the go-between for any offer to the successful candidate, negotiating on behalf of both parties when required.</p><p>We will also provide any unsuccessful candidates with constructive feedback as to why they were not successful. This ensures they are still left with a very positive impression of you and us.</p></div>
      </div>
      <div class="step" style="left:16px;top:185px;width:218px">
        <div class="step__icon"><svg viewBox="0 0 16 16"><path d="M3 8a5 5 0 0 1 8.5-3.5" fill="none" stroke="#7c1a45" stroke-width="1.6"/><polygon points="12.8,2 13,6.2 9,5.2" fill="#7c1a45"/><path d="M13 8a5 5 0 0 1-8.5 3.5" fill="none" stroke="#7c1a45" stroke-width="1.6"/><polygon points="3.2,14 3,9.8 7,10.8" fill="#7c1a45"/></svg></div>
        <div class="step__body"><h3>Follow-up</h3><p>we will keep in touch with the candidate prior to start date and help guide them on handing in their notice and dealing with any counter-offers.</p><p>We will also follow-up with both you and the candidate after they have started to make sure both parties are happy.</p></div>
      </div>
      <div class="photo" role="img" aria-label="Photo seen from above of two businessmen at a grey table reviewing a blue folder of documents" style="left:21px;top:235px;width:209px;height:102px;background:linear-gradient(120deg,#3b3d44 0%,#8d9096 35%,#2f5fa8 55%,#b9bcc1 75%,#262a36 100%)"></div>
    </div>
  </section>

</div>
</body>
</html>
```